Toravel Project Consulting

I need a logo and business card design for a small business operating in the management consulting and contractor space, predominantly in local and state government. I specialise in project management, financial consulting, people and culture, procurement, ICT transformation and contracting for corporate support areas of organisations.

Industry/Entity Type

Business

```html
<!DOCTYPE html>
<html lang="en">
<head>
<meta charset="utf-8">
<title>Toravel Project Consulting – Business Card</title>
<link rel="stylesheet" href="https://fonts.googleapis.com/css2?family=Montserrat:wght@400;700;800&display=swap">
<style>
  :root {
    --bg: #c4e5da;
    --card: #ffffff;
    --red: #e5202b;
    --grey: #8e8f91;
    --shadow: rgba(40, 90, 80, 0.18);
  }
  * { margin: 0; padding: 0; box-sizing: border-box; }
  html, body {
    width: 1200px;
    height: 856px;
    overflow: hidden;
    background: var(--bg);
    font-family: "Montserrat", Arial, sans-serif;
  }
  .stage {
    width: 1200px;
    height: 856px;
    display: flex;
    align-items: center;
    justify-content: center;
    gap: 60px;
  }
  .card {
    position: relative;
    width: 520px;
    height: 297px;
    background: var(--card);
    border-radius: 26px;
    box-shadow: 0 10px 28px var(--shadow);
    overflow: hidden;
  }

  /* Front */
  .card-front {
    display: flex;
    align-items: center;
    justify-content: center;
  }
  .brand-lockup {
    display: flex;
    align-items: center;
    gap: 16px;
  }
  .brand-square {
    width: 40px;
    height: 40px;
    background: var(--red);
    flex: none;
  }
  .brand-name {
    color: var(--grey);
    font-weight: 800;
    font-size: 30px;
    line-height: 1.1;
    letter-spacing: 1px;
    text-transform: uppercase;
  }

  /* Back */
  .wave {
    position: absolute;
    inset: 0;
    width: 100%;
    height: 100%;
  }
  .contact {
    position: absolute;
    top: 40px;
    left: 100px;
    display: flex;
    align-items: center;
    color: var(--red);
  }
  .person {
    text-align: right;
    padding-right: 16px;
  }
  .person-name {
    font-weight: 700;
    font-size: 17px;
    letter-spacing: 0.5px;
  }
  .person-role {
    font-weight: 400;
    font-size: 14px;
  }
  .divider {
    width: 1.5px;
    height: 52px;
    background: var(--red);
  }
  .address {
    padding-left: 16px;
    font-size: 14px;
    line-height: 1.35;
    font-weight: 400;
  }
  .brand-small {
    position: absolute;
    right: 34px;
    bottom: 92px;
    display: flex;
    align-items: center;
    gap: 8px;
  }
  .brand-small .brand-square { width: 16px; height: 16px; }
  .brand-small .brand-name { font-size: 13px; letter-spacing: 0.5px; }
</style>
</head>
<body>
<main class="stage">
  <section class="card card-front" aria-label="Card front">
    <div class="brand-lockup">
      <span class="brand-square"></span>
      <span class="brand-name">Toravel<br>Project<br>Consulting</span>
    </div>
  </section>

  <section class="card card-back" aria-label="Card back">
    <svg class="wave" viewBox="0 0 520 297" preserveAspectRatio="none" aria-hidden="true">
      <path d="M0 212 C 140 198, 220 178, 300 145 S 440 112, 520 108" fill="none" stroke="var(--red)" stroke-width="7"/>
    </svg>
    <div class="contact">
      <div class="person">
        <p class="person-name">PETER HOLLIS</p>
        <p class="person-role">Director</p>
      </div>
      <span class="divider"></span>
      <div class="address">
        <p>14 Marlowe Street</p>
        <p>Westbrook NSW 2190</p>
      </div>
    </div>
    <div class="brand-small">
      <span class="brand-square"></span>
      <span class="brand-name">Toravel<br>Project Consulting</span>
    </div>
  </section>
</main>
</body>
</html>
```